Double Sided Business Card Design for Pet Services

My mom and I want to start a business for pets. We want to offer dog walking, pet sitting as well as boarding and grooming at our home. For the front of the business card, we want a logo that will capture all of our services. We want the name to be Bigotes, Inc., which means little paws in Spanish. Perhaps, there could be little paws or just a little paw implemented within the word Bigotes. Or we would want a cat and a dog by the word Bigotes. We have a cat and a dog at home, and we would be really happy if they could be a part of the business card. It does not have to be anything crazy. Just an outline of a cat or a dog would be awesome. Please see uploaded file.
As for the back of the card, we would want little paws all over the card or we would want a collar, leash, grooming scissor, dog/cat bowl, bone, fish, or toy to show all of the services that we provide. Along with either the many paws or many pet objects, we would want to add our information, such as name (Lorenza Mireles), telephone numbers (555) 812-3762, e-mail addresses bigotesinc@correomail.net, etc.
We would also want a catch phrase to go on the back of the card, such as "Where all paws matter!" Or "We strive for happy tails." or "A paw-bulous service is guaranteed!"
As for colors, we would not want that many. We would want perhaps white and blue. We would want soft colors that will stand out and make an impression. The same goes with the text. An elegant text would be nice. Or perhaps a text with bold letters. We are excited to see the results, but we are also excited to see your creative ideas and what you will bring to the table.

Target Market(s)

Pet Owners

Contact Information for Business Card

For the front of the business card, we want a logo that will capture all of our services. We want the name to be Bigotes, Inc., which means little paws in Spanish. Perhaps, there could be little paws or just a little paw implemented within the word Bigotes. Or we would want a cat and a dog by the word Bigotes. We have a cat and a dog at home, and we would be really happy if they could be a part of the business card. It does not have to be anything crazy. Just an outline of a cat or a dog would be awesome. Please see uploaded file.
As for the back of the card, we would want little paws all over the card or we would want a collar, leash, grooming scissor, dog/cat bowl, bone, fish, or toy to show all of the services that we provide. Along with either the many paws or many pet objects, we would want to add our information, such as name, telephone numbers, e-mail addresses, etc. We would also want a catch phrase to go on the back of the card, such as "Where all paws matter!" Or "We strive happy tails." or "A paw-bulous service is guaranteed!" Or if there is a way to put the catch phrase in the front of the card. We are open to seeing variety.

Logo Text

Bigotes, Inc

Font styles to use
Serif
Script

Colors
ffffff
33a6d7
145ea8

Requirements
Must have
• My project must be a double sided business card.

```html
<!DOCTYPE html>
<html lang="en">
<head>
<meta charset="utf-8">
<title>Bigotes, Inc — Business Card</title>
<link rel="stylesheet" href="https://fonts.googleapis.com/css2?family=Yellowtail&family=Kaushan+Script&family=Montserrat:wght@300;400;600&display=swap">
<style>
  :root {
    --page: #ffffff;
    --card-blue: #145ea8;
    --pattern-blue: #2168b0;
    --ink-white: #ffffff;
    --ink-soft: #d6e6f5;
  }
  * { margin: 0; padding: 0; box-sizing: border-box; }
  html, body {
    width: 1200px;
    height: 800px;
    overflow: hidden;
    background: var(--page);
  }
  .canvas {
    position: relative;
    width: 1200px;
    height: 800px;
  }
  .card {
    position: absolute;
    left: 337px;
    width: 525px;
    height: 340px;
    background: var(--card-blue);
    color: var(--ink-white);
    overflow: hidden;
  }
  .card--front { top: 42px; }
  .card--back { top: 418px; }

  .brand {
    position: absolute;
    inset: 0;
  }
  .brand__mark {
    position: absolute;
    left: 50%;
    top: 64px;
    width: 124px;
    height: 124px;
    margin-left: -62px;
    border-radius: 50%;
    background: var(--ink-white);
  }
  .brand__name {
    position: absolute;
    left: 0;
    right: 0;
    top: 208px;
    text-align: center;
    font-family: "Yellowtail", "Kaushan Script", cursive;
    font-weight: 400;
    font-size: 56px;
    line-height: 1.2;
    color: var(--ink-white);
  }
  .brand__tagline {
    position: absolute;
    right: 152px;
    top: 266px;
    font-family: "Montserrat", sans-serif;
    font-weight: 300;
    font-size: 18px;
    line-height: 1.2;
    color: var(--ink-soft);
  }

  .paw-pattern {
    position: absolute;
    inset: 0;
    background: radial-gradient(circle at 50% 50%, var(--pattern-blue) 0%, var(--card-blue) 80%);
  }
  .contact {
    position: absolute;
    inset: 0;
    text-align: center;
  }
  .contact__name {
    position: absolute;
    left: 0;
    right: 0;
    top: 124px;
    font-family: "Yellowtail", "Kaushan Script", cursive;
    font-size: 46px;
    font-weight: 400;
    line-height: 1.2;
    color: var(--ink-white);
  }
  .contact__details {
    position: absolute;
    left: 0;
    right: 0;
    top: 185px;
    font-family: "Montserrat", sans-serif;
    font-weight: 400;
    font-size: 18px;
    line-height: 1.2;
    color: var(--ink-white);
  }
  .contact__divider { margin: 0 18px; }
  .contact__motto {
    position: absolute;
    left: 0;
    right: 0;
    top: 277px;
    font-family: "Montserrat", sans-serif;
    font-weight: 400;
    font-size: 17px;
    line-height: 1.2;
    color: var(--ink-white);
  }
</style>
</head>
<body>
<main class="canvas">
  <section class="card card--front" aria-label="Card front">
    <div class="brand">
      <span class="brand__mark" aria-hidden="true"></span>
      <p class="brand__name">Bigotes, Inc</p>
      <p class="brand__tagline">pet services</p>
    </div>
  </section>

  <section class="card card--back" aria-label="Card back">
    <div class="paw-pattern" role="img" aria-label="Faint scattered paw print pattern across the card"></div>
    <div class="contact">
      <h1 class="contact__name">Lorenza Mireles</h1>
      <p class="contact__details">
        <span class="contact__phone">(555) 812-3762</span><span class="contact__divider">|</span><span class="contact__email">bigotesinc@correomail.net</span>
      </p>
      <p class="contact__motto">“a paw-bulous service is guranteed!”</p>
    </div>
  </section>
</main>
</body>
</html>
```